Figure for a research paper

I am working on designing a figure for a research paper that illustrates the effect of KADO Pathways assessment on student outcomes over time by impacting teacher bias and teacher perception of student growth. I built the attached figure via powerpoint. It includes the very basic elements but it does not look great and I am not sure that it is clearly depicting what I am hoping to illustrate. I would like for you to build an illustration of this idea that i can include in the paper.

```html
<!DOCTYPE html>
<html lang="en">
<head>
<meta charset="utf-8">
<title>KADO Pathways Assessment and Perceived SEL Effectiveness Over Time</title>
<link rel="stylesheet" href="https://fonts.googleapis.com/css2?family=Source+Serif+4:wght@600;700&display=swap">
<style>
  :root {
    --navy: #17607f;
    --red: #ff0000;
    --paper: #ffffff;
  }
  html, body {
    margin: 0;
    padding: 0;
    width: 1059px;
    height: 1200px;
    overflow: hidden;
    background: var(--paper);
  }
  .figure {
    display: block;
    width: 1059px;
    height: 1200px;
  }
  .axis-bar { fill: var(--navy); }
  .axis-title {
    fill: var(--paper);
    font-family: "Source Serif 4", Georgia, serif;
    font-weight: 600;
    font-size: 36px;
    text-anchor: middle;
  }
  .axis-title--y { font-size: 34px; }
  .trend { fill: none; stroke-linecap: butt; }
  .trend--perceived { stroke: var(--red); stroke-width: 11; }
  .trend--actual { stroke: var(--navy); stroke-width: 11; }
  .trend--single { stroke: var(--navy); stroke-width: 7; }
  .callout-box { fill: var(--paper); stroke: var(--navy); stroke-width: 4; }
  .callout-text {
    fill: var(--navy);
    font-family: "Source Serif 4", Georgia, serif;
    font-weight: 700;
    font-size: 28px;
    text-anchor: middle;
  }
  .connector { stroke: var(--navy); stroke-width: 4; fill: none; }
  .arrowhead { fill: var(--navy); }
</style>
</head>
<body>
<svg class="figure" viewBox="0 0 1800 2040" xmlns="http://www.w3.org/2000/svg" role="img"
     aria-label="Two charts of SEL program effectiveness on the student over time, with and without the KADO Pathways Assessment">

  <!-- Panel A: with assessment -->
  <g class="panel panel--with-assessment">
    <rect class="axis-bar" x="224" y="125" width="96" height="807"/>
    <rect class="axis-bar" x="224" y="836" width="1356" height="96"/>
    <text class="axis-title" x="893" y="898">Time</text>
    <text class="axis-title axis-title--y" transform="translate(272 522) rotate(-90)">
      <tspan x="0" y="-6">Effectiveness of SEL Program</tspan>
      <tspan x="0" y="32">on the Student</tspan>
    </text>

    <line class="trend trend--actual" x1="385" y1="781" x2="1495" y2="699"/>
    <line class="trend trend--perceived" x1="385" y1="778" x2="1490" y2="449"/>

    <g class="callout callout--perception">
      <rect class="callout-box" x="927" y="366" width="476" height="71"/>
      <text class="callout-text" x="1165" y="394">Teacher’s inaccurate perception of</text>
      <text class="callout-text" x="1165" y="422">student growth or learning</text>
      <line class="connector" x1="1165" y1="437" x2="1165" y2="515"/>
      <path class="arrowhead" d="M1165 527 L1151 502 L1165 511 L1179 502 Z"/>
    </g>

    <g class="callout callout--bias">
      <rect class="callout-box" x="578" y="528" width="190" height="50"/>
      <text class="callout-text" x="673" y="561">Teacher Bias</text>
      <line class="connector" x1="673" y1="578" x2="673" y2="655"/>
      <path class="arrowhead" d="M673 667 L659 642 L673 651 L687 642 Z"/>
    </g>

    <g class="callout callout--assessment">
      <rect class="callout-box" x="1122" y="608" width="380" height="50"/>
      <text class="callout-text" x="1309" y="641">KADO Pathways Assessment</text>
      <line class="connector" x1="1317" y1="608" x2="1317" y2="531"/>
      <path class="arrowhead" d="M1317 519 L1303 544 L1317 535 L1331 544 Z"/>
    </g>
  </g>

  <!-- Panel B: without assessment -->
  <g class="panel panel--without-assessment">
    <rect class="axis-bar" x="224" y="1112" width="96" height="807"/>
    <rect class="axis-bar" x="224" y="1823" width="1356" height="96"/>
    <text class="axis-title" x="893" y="1885">Time</text>
    <text class="axis-title axis-title--y" transform="translate(272 1509) rotate(-90)">
      <tspan x="0" y="-6">Effectiveness of SEL Program</tspan>
      <tspan x="0" y="32">on the Student</tspan>
    </text>

    <line class="trend trend--single" x1="320" y1="1662" x2="1472" y2="1463"/>

    <g class="callout callout--perception">
      <rect class="callout-box" x="927" y="1334" width="476" height="71"/>
      <text class="callout-text" x="1165" y="1362">Teacher’s inaccurate perception of</text>
      <text class="callout-text" x="1165" y="1390">student growth or learning</text>
      <line class="connector" x1="1165" y1="1405" x2="1165" y2="1483"/>
      <path class="arrowhead" d="M1165 1495 L1151 1470 L1165 1479 L1179 1470 Z"/>
    </g>

    <g class="callout callout--bias">
      <rect class="callout-box" x="578" y="1442" width="190" height="50"/>
      <text class="callout-text" x="673" y="1475">Teacher Bias</text>
      <line class="connector" x1="673" y1="1492" x2="673" y2="1569"/>
      <path class="arrowhead" d="M673 1581 L659 1556 L673 1565 L687 1556 Z"/>
    </g>
  </g>
</svg>
</body>
</html>
```